Label designs for three different cider varieties

The Larkmoor Perry Works is a family run business. We have been making cider within the family as a hobby for over 100 years and we have recently decided to start to try to sell the cider. Therefore this project is to create a logo and three product labels for three different varieties of cider. So we should end up with four files; one for the logo and one for each of the labels. The files need to be in an editable format for us so that we can add edit the batch numbers e.g. PNG file.
For the logo we would like to use the Pellow Family Shield since Pellow is our family name. We would like it adapted into a cider themed crest, for example with apples and trees. We are open to ideas about the logo but this is just our initial idea. Example of the original Pellow Family Shield can be seen in the link below:
http://www.vinshadeheraldry.net/arms/Pellow-England.jpg
The labels should be no bigger than 93mm in height and 213mm in length. Each label should be similar in style so it is clear the three different varieties of cider are from the same company. Each label must have the following information since this is a legal requirement:
- The logo you have created
- The Larkmoor Perry Works Ltd.
- 52 Mirefield Row, Taunton, Somerset, TA4 9QX
- Alcohol: 6% vol
- 500ml
- Allergens: Contains Sulphites for freshness
- There needs to be space on the label for batch numbers. This is four numbers e.g. 1701.
- Family craft cider makers using only premium apples from our own traditional Somerset orchard.
The names of the three cider varieties are:
- Larkmoor Heritage
- Larkmoor Amber
- Larkmoor Kingsbury
Our initial idea is that each variety would have its own colour associated with it; i.e. black themed label for Larkmoor Heritage, gold themed label for Larkmoor Amber and a red themed label for Larkmoor Kingsbury. The crest logo you have created would then be in the themed colour for that cider variety i.e. black, gold or red.
We would like the labels to reflect the following themes for our brand:
- High end premium brand
- Clean and simple design
- Modern
Overall we are very open to ideas and we do not want to constrain your creativity. All of the above is just our initial ideas but we would love to see what ideas you have. The only things that cannot change are what must be on the label since this is a legal requirement we have to meet.

```html
<!DOCTYPE html>
<html lang="en">
<head>
<meta charset="utf-8">
<title>Larkmoor Perry Works – Cider Labels</title>
<link rel="stylesheet" href="https://fonts.googleapis.com/css2?family=Anton&family=Montserrat:wght@600;700&family=Oswald:wght@500;600&display=swap">
<style>
  :root{
    --canvas:#ffffff;
    --heritage:#42413d;
    --amber:#766c33;
    --kingsbury:#74131a;
    --ink:#1f1f1d;
    --cream:#f2f1e8;
    --rule:#ffffff;
    --art-tone:rgba(0,0,0,.14);
  }
  *{box-sizing:border-box;margin:0;padding:0}
  html,body{width:1200px;height:1000px;overflow:hidden;background:var(--canvas)}
  .sheet{position:relative;width:1200px;height:1000px}
  .label{position:absolute;left:213px;width:757px;height:328px;overflow:hidden;color:var(--ink);border:1px solid #2a2a28}
  .label--heritage{top:0;background:var(--heritage)}
  .label--amber{top:336px;background:var(--amber)}
  .label--kingsbury{top:674px;height:326px;background:var(--kingsbury)}

  .art-area{position:absolute;background:var(--art-tone)}
  .art-area--left{left:12px;top:78px;width:210px;height:180px}
  .art-area--right{left:535px;top:78px;width:210px;height:180px}
  .art-area--crest{left:334px;top:8px;width:92px;height:72px}

  .brand-mark__square{position:absolute;left:362px;top:10px;width:34px;height:34px;background:var(--cream);border:2px solid var(--ink)}
  .brand-mark__tag{position:absolute;left:0;width:100%;top:84px;text-align:center;font:600 7px/1 "Montserrat",sans-serif;letter-spacing:.5px}
  .brand-mark__name{position:absolute;left:0;width:100%;top:93px;text-align:center;font:700 9px/1 "Montserrat",sans-serif;letter-spacing:.3px}

  .variety{position:absolute;left:0;width:100%;top:113px;text-align:center;font:700 30px/1 "Montserrat",sans-serif;letter-spacing:.5px;white-space:nowrap}
  .variety-rule{position:absolute;left:247px;width:278px;top:147px;height:5px;background:var(--ink)}
  .product{position:absolute;left:0;width:100%;top:154px;text-align:center;font:400 86px/1 "Anton",sans-serif;letter-spacing:4px}
  .abv{position:absolute;left:493px;top:230px;font:600 10px/1 "Oswald",sans-serif}

  .info-box{position:absolute;left:252px;top:245px;width:271px;height:71px;border:1px solid var(--rule)}
  .info-box__story{position:absolute;left:3px;top:6px;width:108px;font:600 7.5px/11.5px "Oswald",sans-serif;text-align:justify;text-align-last:center}
  .info-box__bar{position:absolute;left:3px;top:56px;width:108px;height:5px;background:var(--ink)}
  .info-box__claims{position:absolute;left:113px;top:6px;width:156px;text-align:center;font:600 16px/20px "Oswald",sans-serif;letter-spacing:.3px}
  .info-box__serve{font-size:11.5px;line-height:16px}

  .batch-box{position:absolute;left:16px;top:262px;width:74px;height:31px;background:var(--cream)}
  .volume{position:absolute;left:16px;top:302px;font:600 13px/1 "Oswald",sans-serif}
  .allergens{position:absolute;left:58px;top:307px;font:600 6.5px/1 "Oswald",sans-serif}
  .maker-box{position:absolute;left:548px;top:290px;width:197px;height:29px;background:var(--cream);padding:4px 5px;font:600 7.5px/11px "Oswald",sans-serif;white-space:nowrap}
</style>
</head>
<body>
<main class="sheet">

  <section class="label label--heritage">
    <div class="art-area art-area--left" role="img" aria-label="Etched illustration of an old orchard apple tree"></div>
    <div class="art-area art-area--right" role="img" aria-label="Etched illustration of an old orchard apple tree"></div>
    <div class="art-area art-area--crest" role="img" aria-label="Small orchard tree behind the brand mark"></div>
    <span class="brand-mark__square"></span>
    <p class="brand-mark__tag">ORCHARD &amp; CIDERY</p>
    <p class="brand-mark__name">LARKMOOR PERRY WORKS</p>
    <h2 class="variety">LARKMOOR HERITAGE</h2>
    <div class="variety-rule"></div>
    <h1 class="product">CIDER</h1>
    <p class="abv">6% VOL</p>
    <div class="info-box">
      <p class="info-box__story">FAMILY CRAFT CIDER MAKERS USING ONLY PREMIUM APPLES FROM OUR OWN TRADITIONAL SOMERSET ORCHARD.</p>
      <div class="info-box__bar"></div>
      <p class="info-box__claims">SMALL BATCH CIDER<br>FROM SOMERSET<br><span class="info-box__serve">******ENJOY CHILLED******</span></p>
    </div>
    <div class="batch-box"></div>
    <p class="volume">500ml</p>
    <p class="allergens">ALLERGENS: CONTAINS SULPHITES FOR FRESHNESS</p>
    <p class="maker-box">THE LARKMOOR PERRY WORKS LTD.<br>52 MIREFIELD ROW, TAUNTON, SOMERSET, TA4 9QX</p>
  </section>

  <section class="label label--amber">
    <div class="art-area art-area--left" role="img" aria-label="Etched illustration of an old orchard apple tree"></div>
    <div class="art-area art-area--right" role="img" aria-label="Etched illustration of an old orchard apple tree"></div>
    <div class="art-area art-area--crest" role="img" aria-label="Small orchard tree behind the brand mark"></div>
    <span class="brand-mark__square"></span>
    <p class="brand-mark__tag">ORCHARD &amp; CIDERY</p>
    <p class="brand-mark__name">LARKMOOR PERRY WORKS</p>
    <h2 class="variety">LARKMOOR AMBER</h2>
    <div class="variety-rule"></div>
    <h1 class="product">CIDER</h1>
    <p class="abv">6% VOL</p>
    <div class="info-box">
      <p class="info-box__story">FAMILY CRAFT CIDER MAKERS USING ONLY PREMIUM APPLES FROM OUR OWN TRADITIONAL SOMERSET ORCHARD.</p>
      <div class="info-box__bar"></div>
      <p class="info-box__claims">SMALL BATCH CIDER<br>FROM SOMERSET<br><span class="info-box__serve">******ENJOY CHILLED******</span></p>
    </div>
    <div class="batch-box"></div>
    <p class="volume">500ml</p>
    <p class="allergens">ALLERGENS: CONTAINS SULPHITES FOR FRESHNESS</p>
    <p class="maker-box">THE LARKMOOR PERRY WORKS LTD.<br>52 MIREFIELD ROW, TAUNTON, SOMERSET, TA4 9QX</p>
  </section>

  <section class="label label--kingsbury">
    <div class="art-area art-area--left" role="img" aria-label="Etched illustration of an old orchard apple tree"></div>
    <div class="art-area art-area--right" role="img" aria-label="Etched illustration of an old orchard apple tree"></div>
    <div class="art-area art-area--crest" role="img" aria-label="Small orchard tree behind the brand mark"></div>
    <span class="brand-mark__square"></span>
    <p class="brand-mark__tag">ORCHARD &amp; CIDERY</p>
    <p class="brand-mark__name">LARKMOOR PERRY WORKS</p>
    <h2 class="variety">LARKMOOR KINGSBURY</h2>
    <div class="variety-rule"></div>
    <h1 class="product">CIDER</h1>
    <p class="abv">6% VOL</p>
    <div class="info-box">
      <p class="info-box__story">FAMILY CRAFT CIDER MAKERS USING ONLY PREMIUM APPLES FROM OUR OWN TRADITIONAL SOMERSET ORCHARD.</p>
      <div class="info-box__bar"></div>
      <p class="info-box__claims">SMALL BATCH CIDER<br>FROM SOMERSET<br><span class="info-box__serve">******ENJOY CHILLED******</span></p>
    </div>
    <div class="batch-box"></div>
    <p class="volume">500ml</p>
    <p class="allergens">ALLERGENS: CONTAINS SULPHITES FOR FRESHNESS</p>
    <p class="maker-box">THE LARKMOOR PERRY WORKS LTD.<br>52 MIREFIELD ROW, TAUNTON, SOMERSET, TA4 9QX</p>
  </section>

</main>
</body>
</html>
```